Web design for a Crane & Heavy Equipment Inspection, Repair and Maintenance Company in Texas

We need a web design for a new company based in Houston, Texas called "Bristen Hoist & Equipment". We inspect, repair and maintain diesel driven heavy equipment, generators, fire water pumps and cranes. We would like to see designs that use the colors orange, white, yellow and brown, and/or orange, white, navy, yellow and grey.

```html
<!DOCTYPE html>
<html lang="en">
<head>
<meta charset="utf-8">
<title>Bristen Hoist &amp; Equipment</title>
<link href="https://fonts.googleapis.com/css2?family=Lato:wght@300;400;700&family=Cabin+Condensed:wght@500;600&family=Arimo&display=swap" rel="stylesheet">
<style>
:root{
  --orange:#f05a28;
  --orange-dark:#d2461b;
  --navy:#1b4f85;
  --blue:#2e5f93;
  --text:#555;
  --heading:#333;
  --band:#ececec;
  --footer:#2b2b2b;
  --white:#fff;
  --photo-warm:#d8b448;
  --photo-cool:#9dbbd6;
  --thumb:#a9b9c6;
}
*{margin:0;padding:0;box-sizing:border-box}
html,body{width:939px;height:1200px;overflow:hidden;background:var(--white)}
body{position:relative;font-family:"Lato",sans-serif;color:var(--text)}
.abs{position:absolute}
.brand{left:68px;top:58px;display:flex;align-items:center;gap:12px;font-weight:700;font-size:30px;color:var(--navy);white-space:nowrap}
.brand-mark{width:22px;height:22px;background:var(--orange)}
.top-phone{right:68px;top:52px;font-size:19px;color:var(--navy);display:flex;align-items:center;gap:10px}
.search{left:667px;top:100px;width:204px;height:28px;border:1px solid #d4d4d4;font-size:12px;color:#888;padding:7px 10px;display:flex;justify-content:space-between;align-items:center}
.nav{left:68px;top:161px;width:803px;height:45px;background:var(--orange);display:flex}
.nav a{height:45px;display:flex;align-items:center;justify-content:center;color:var(--white);text-decoration:none;font-weight:700;font-size:13.5px;border-right:1px solid #e04f20;text-shadow:0 1px 1px rgba(0,0,0,.25)}
.nav a.active{background:var(--orange-dark)}
.hero{left:69px;top:206px;width:802px;height:354px;overflow:hidden}
.hero-photo{position:absolute;inset:0;background:linear-gradient(100deg,var(--photo-cool) 0%,var(--photo-warm) 45%,#c9b46a 100%)}
.hero-title{left:539px;top:152px;font-family:"Cabin Condensed",sans-serif;font-weight:600;font-size:31px;color:var(--white)}
.hero-text{left:539px;top:196px;width:230px;font-size:13.5px;line-height:21px;color:var(--white)}
.dots{left:692px;top:303px;display:flex;gap:4px}
.dots span{width:13px;height:13px;border-radius:50%;background:rgba(255,255,255,.55)}
.dots span:first-child{background:var(--white)}
.feature-icon{width:82px;height:82px;border-radius:50%;background:#f1f1f1;border:3px solid #fff;box-shadow:0 0 0 1px #d8d8d8;display:flex;align-items:center;justify-content:center}
.feature-title{font-size:18px;color:var(--heading)}
.feature-text{font-size:11.8px;line-height:19px;width:150px;color:#555;margin-top:6px}
.section-title{font-size:22px;font-weight:300;color:var(--heading)}
.about-text{left:68px;top:803px;width:477px;font-size:11.6px;line-height:18.8px;color:#666}
.about-text p+p{margin-top:7px}
.news-item{left:601px;width:268px;display:flex;gap:15px}
.news-thumb{width:83px;height:60px;border:3px solid #fff;box-shadow:0 0 0 1px #ddd;flex:none;background:var(--thumb)}
.news-title{font-size:11.4px;color:var(--orange);margin-top:2px;white-space:nowrap}
.news-text{font-size:11.2px;line-height:18px;color:#444;margin-top:4px;white-space:nowrap}
.news-rule{left:601px;top:878px;width:268px;border-top:1px dotted #bbb}
.contact-band{left:0;top:1017px;width:939px;height:89px;background:var(--band);font-family:"Arimo",sans-serif}
.band-item{position:absolute;top:0;height:89px;display:flex;align-items:center;gap:14px;color:#555;font-size:13px}
.band-sep{position:absolute;top:29px;width:1px;height:36px;background:#ccc}
.footer{left:0;top:1106px;width:939px;height:94px;background:var(--footer);color:var(--white);font-family:"Arimo",sans-serif;font-size:11.8px}
.social{position:absolute;top:34px;width:28px;height:28px}
</style>
</head>
<body>

<div class="abs brand"><span class="brand-mark"></span>Bristen Hoist &amp; Equipment</div>

<div class="abs top-phone">+1 713 555 0142
  <svg width="16" height="20" viewBox="0 0 16 20"><path d="M4 1l3 4-2 2c1 3 3 6 6 8l2-2 3 3-3 3C7 18 1 11 1 4z" fill="var(--navy)"/></svg>
</div>

<div class="abs search">Search..
  <svg width="11" height="11" viewBox="0 0 11 11"><circle cx="4.5" cy="4.5" r="3.5" fill="none" stroke="#999" stroke-width="1.5"/><path d="M7 7l3.5 3.5" stroke="#999" stroke-width="1.5"/></svg>
</div>

<nav class="abs nav">
  <a class="active" href="#" style="width:95px">HOME</a>
  <a href="#" style="width:91px">ABOUT</a>
  <a href="#" style="width:103px">CRANES</a>
  <a href="#" style="width:172px">SERVICES OFFERED</a>
  <a href="#" style="width:86px">BLOG</a>
  <a href="#" style="width:147px">TESTIMONIALS</a>
  <a href="#" style="width:109px;border-right:none">CONTACT</a>
</nav>

<section class="abs hero">
  <div class="hero-photo" role="img" aria-label="Photo of a yellow mobile crane truck on an airfield"></div>
  <svg class="abs" style="left:0;top:0" width="802" height="354"><polygon points="631,0 802,0 802,354 382,354" fill="var(--blue)" opacity=".92"/><line x1="631" y1="0" x2="382" y2="354" stroke="#fff" stroke-opacity=".5" stroke-width="4"/></svg>
  <div class="abs hero-title">AENEAN COMDO</div>
  <div class="abs hero-text">Eodem modo typi, qui nunc nobis vide ntur parum clari, fiant sollemnes infut.</div>
  <div class="abs dots"><span></span><span></span><span></span><span></span></div>
</section>

<div class="abs feature-icon" style="left:68px;top:616px">
  <svg width="46" height="46" viewBox="0 0 46 46"><g fill="var(--orange)"><circle cx="23" cy="23" r="14"/><rect x="19" y="2" width="8" height="42"/><rect x="2" y="19" width="42" height="8"/><rect x="19" y="2" width="8" height="42" transform="rotate(45 23 23)"/><rect x="19" y="2" width="8" height="42" transform="rotate(-45 23 23)"/></g><circle cx="23" cy="23" r="6" fill="#f1f1f1"/></svg>
</div>
<div class="abs" style="left:168px;top:614px"><div class="feature-title">Inspect</div><div class="feature-text">Claritas est etiam processna micus, qui sequitur mutaem consuetudium lectorum</div></div>

<div class="abs feature-icon" style="left:349px;top:616px">
  <svg width="46" height="46" viewBox="0 0 46 46"><path d="M40 4C30 4 22 10 16 20l10 10c10-6 16-14 14-26zM14 22l-8 2 4 4zM24 32l-2 8-4-4zM12 30c-4 2-6 8-6 10 2 0 8-2 10-6z" fill="var(--orange)"/></svg>
</div>
<div class="abs" style="left:449px;top:614px"><div class="feature-title">Repair</div><div class="feature-text">Claritas est etiam processna micus, qui sequitur mutaem consuetudium lectorum</div></div>

<div class="abs feature-icon" style="left:634px;top:616px">
  <svg width="46" height="46" viewBox="0 0 46 46"><path d="M4 22C4 12 12 6 23 6s19 6 19 16z" fill="var(--orange)"/><path d="M23 22v14c0 4-6 4-6 0" fill="none" stroke="var(--orange)" stroke-width="2.5"/></svg>
</div>
<div class="abs" style="left:735px;top:614px"><div class="feature-title">Maintain</div><div class="feature-text">Claritas est etiam processna micus, qui sequitur mutaem consuetudium lectorum</div></div>

<h2 class="abs section-title" style="left:68px;top:755px">Welcome to Our Website</h2>
<div class="abs about-text">
  <p>Eu tortor euismodolo. Vestibulum ant psu meop primis inicibu orci luctus ed ultrices et pos uere cubil. Cura sed quis nibhut odiocinialor matis ed iaculis ante sed vel laciniate. Eu tortir euismodolo. Vestibulum ant psu meop primis inicibu orci luctus ed ultrices et posuere cuul Cura sed quis nibhut odiocinialor matis ed iaculis ante sed vel laciniate.</p>
  <p>Eu tortor euismodolo. Vestibulum ant psu meop primis inicibu orci luctus ed ultrices et pos uere cubil. Cura sed quis nibhut odiocinialor matis ed iaculis ante sed vel laciniate. Eu toirtr euismodolo. Vestibulum ant psu meop primis inicibu orci luctus ed ultrices et posuere cubi l. Cura sed quis nibhut odiocinialor matis ed iaculis ante sed vel laciniate. Eu tortor</p>
</div>

<h2 class="abs section-title" style="left:601px;top:755px">Latest News</h2>
<div class="abs news-item" style="top:801px">
  <div class="news-thumb" role="img" aria-label="Photo of a yellow mobile crane with extended boom"></div>
  <div><div class="news-title">Duis autem vel eum iriure dolor</div><div class="news-text">Brianne craves the endorphin rufu<br>eled by fitness and uses it.</div></div>
</div>
<div class="abs news-rule"></div>
<div class="abs news-item" style="top:895px">
  <div class="news-thumb" role="img" aria-label="Photo of tower cranes at a harbour construction site"></div>
  <div><div class="news-title">Duis autem vel eum iriure dolor</div><div class="news-text">Brianne craves the endorphin ruifu<br>eled by fitness and uses it.</div></div>
</div>

<section class="abs contact-band">
  <div class="band-item" style="left:90px">
    <svg width="22" height="30" viewBox="0 0 22 30"><path d="M11 1C5 1 1 5 1 11c0 7 10 18 10 18s10-11 10-18C21 5 17 1 11 1z" fill="#555"/><circle cx="11" cy="11" r="4" fill="var(--band)"/></svg>
    <div><div style="font-size:13.5px">Duis autem vel eum iriureHendrerit.</div><div style="font-size:11.5px;margin-top:5px">Typi non habent claritatem insitam</div></div>
  </div>
  <div class="band-sep" style="left:373px"></div>
  <div class="band-item" style="left:418px">
    <svg width="22" height="26" viewBox="0 0 16 20"><path d="M4 1l3 4-2 2c1 3 3 6 6 8l2-2 3 3-3 3C7 18 1 11 1 4z" fill="#555"/></svg>
    <span>713 - 555 - 0198</span>
  </div>
  <div class="band-sep" style="left:583px"></div>
  <div class="band-item" style="left:632px">
    <svg width="36" height="22" viewBox="0 0 36 22"><rect x="1" y="1" width="34" height="20" fill="#555"/><path d="M1 1l17 12L35 1M1 21l13-10M35 21L22 11" fill="none" stroke="var(--band)" stroke-width="1.5"/></svg>
    <span style="font-size:13.5px">info@bristenhoist.com</span>
  </div>
</section>

<footer class="abs footer">
  <div class="abs" style="left:68px;top:24px">Terms and Conditions | Privacy Promise | FAQ's | Contact Us</div>
  <div class="abs" style="left:68px;top:52px">Copyright © 2013. All Rights Reserved.</div>
  <span class="social" style="left:692px;background:#3b5a9a"></span>
  <span class="social" style="left:730px;background:#2d9fd9"></span>
  <span class="social" style="left:768px;background:#f26522"></span>
  <span class="social" style="left:807px;background:#e02a20"></span>
</footer>

</body>
</html>
```